A new Blog: Turning Over New Leaves

I need a wordpress blog design for my new blog called Turning Over New Leaves.

I'm not an alcoholic. I certainly don't think I am, and I'm fairly certain that if you spoke to my friends and family they would agree that I don't have any issues with substance abuse. I definitely enjoy a drink. A few beers, gin and tonic's or a nice red wine (along with a few cigarettes) have been particular vices for the last few years of my life.

But no more. I'm going 365 with no alcohol and I am giving up cigarettes.

Why? I have my reasons... and this blog will reveal those and chronicle my year long journey.

The blog is called Turning Over New Leaves and I want a clean, crisp design to reflect this new adventure.

I'm looking for a design that is unique and not the same as every other blog you see. I want my readers to feel uplifted when they see it.

Most importantly, the blog needs to be simple for me to use and modify (add a new page if needed in the future)
Updates

Reason: To allow time for designers to submit revised designs.

Reason: My apologies designers, I haven't had an opportunity to provide feedback to enable changes. I will be doign this tomorrow morning and so am extending the deadline to allow resubmission.

Regards, Dale.

Target Market(s)

My target market are males and females, 17-28 in western speaking countries

Requirements
Must have
• - A graphic banner/branding featuring the blog title. This should be able to be used as a small stand alone logo.
- Ability to show my latest tweets
- A connect box where people can click on Chatterloop, Peepstream and Postvane links to contact me
- A widget that is showing how many days I am into the 365 day challenge (this should feature prominently)
- A widget that shows how much money as the challenge progresses
- It should have an ability to subcribe to the blog (RSS feeds)
- There needs to be an about me page
- There should be a blog roll
- There should be a list of categories/tags displayed somewhere (do something creative with this, find a way to make what I am talking about most more prominent!)
- A recent post link box somewhere at the side to encourage people to keep reading
- Recent comment links
- A search functionality
- An advertisement side bar (only a small amount of advertising will be done - so don't make it too prominent!)

Nice to have
• Without crowding the design it would also be good to have
-Popular post links (the most highly trafficked or commented) posts.

I'm excited to hear what other things YOU THINK should feature. Surprise me! I will reward innovation.

```html
<!DOCTYPE html>
<html lang="en">
<head>
<meta charset="utf-8">
<title>Turning Over New Leaves — Comment</title>
<link href="https://fonts.googleapis.com/css2?family=Arimo:ital,wght@0,400;0,700;1,400&display=swap" rel="stylesheet">
<style>
  :root {
    --sky-top: #cfe6f6;
    --sky-mid: #f4f6f7;
    --sky-low: #5a9be2;
    --grass-light: #9ad61a;
    --grass-dark: #3f8a12;
    --page: #ffffff;
    --sidebar: #f3f3f3;
    --ink: #111111;
    --block: #222222;
    --muted: #8a8a8a;
    --soft: #a8a8a8;
    --line: #c8c8c8;
    --green-link: #9db56a;
    --rss-brown: #8a5a20;
    --rss-fill: #f1e9dc;
  }
  * { box-sizing: border-box; margin: 0; padding: 0; }
  html, body { width: 1200px; height: 1091px; overflow: hidden; }
  body {
    position: relative;
    font-family: "Arimo", Helvetica, Arial, sans-serif;
    color: var(--ink);
    background: linear-gradient(180deg, var(--sky-top) 0px, var(--sky-mid) 520px, var(--sky-mid) 870px, #bcd9f3 930px, var(--sky-low) 1030px);
  }
  .grass {
    position: absolute; left: 0; bottom: 0; width: 1200px; height: 62px;
    background: linear-gradient(180deg, var(--grass-light) 0%, #6cb316 55%, var(--grass-dark) 100%);
    border-radius: 60% 40% 0 0 / 14px 10px 0 0;
  }
  .page { position: absolute; left: 146px; top: 0; width: 644px; height: 971px; background: var(--page); }
  .sidebar { position: absolute; left: 790px; top: 0; width: 262px; height: 971px; background: var(--sidebar); }
  .top-rule { position: absolute; left: 30px; top: 0; width: 596px; height: 5px; background: #eeeeee; }

  .comment-title { position: absolute; left: 31px; top: 35px; font-size: 29px; font-weight: 400; }
  .field { position: absolute; left: 30px; width: 358px; height: 47px; border: 1px solid var(--ink); display: flex; background: #fff; }
  .field .icon { width: 47px; height: 100%; background: var(--block); display: flex; align-items: center; justify-content: center; }
  .field span { font-style: italic; font-size: 19px; color: #333; padding: 11px 0 0 11px; }
  .field-comment { height: 185px; width: 433px; }
  .field-comment span { padding-top: 10px; }
  .send { position: absolute; left: 30px; top: 452px; width: 114px; height: 47px; background: var(--block); color: #fff; font-size: 28px; display: flex; align-items: center; justify-content: center; }

  .recent-comment { position: absolute; left: 19px; top: 6px; width: 217px; height: 62px; border: 1px solid #cfcfcf; background: #f7f7f7; }
  .recent-comment .avatar { position: absolute; left: 9px; top: 9px; width: 43px; height: 43px; background: linear-gradient(135deg, #b9b2aa, #5d5650); border: 1px solid #ddd; }
  .recent-comment .txt { position: absolute; left: 58px; top: 10px; font-size: 11.5px; line-height: 14px; }
  .recent-comment .title { color: var(--green-link); }
  .recent-comment .excerpt { color: var(--soft); }
  .recent-comment .date { color: var(--muted); font-size: 9.5px; }

  .widget-title { position: absolute; left: 18px; font-size: 15px; font-weight: 700; color: var(--muted); }
  .blogroll { position: absolute; left: 19px; top: 114px; width: 217px; list-style: none; }
  .blogroll li { height: 28.3px; font-size: 12px; color: var(--soft); border-bottom: 1px dotted #bbb; padding-top: 4px; }

  .tags { position: absolute; left: 19px; top: 304px; width: 225px; color: var(--soft); line-height: 28px; }
  .tags span { margin-right: 6px; white-space: nowrap; }

  .tweet { position: absolute; left: 19px; top: 443px; width: 217px; height: 136px; border: 1px solid #cfcfcf; border-radius: 8px; background: #fff; padding: 13px 12px; font-size: 12px; line-height: 18px; color: #333; }
  .tweet .when { color: var(--muted); }
  .tweet-tail { position: absolute; left: 120px; top: 578px; }
  .mascot { position: absolute; left: 174px; top: 562px; width: 52px; height: 66px; border-radius: 50% 50% 45% 45%; background: radial-gradient(circle at 45% 35%, #6fd2f5, #1d8fd0); }
  .mascot-shadow { position: absolute; left: 115px; top: 620px; width: 120px; height: 10px; border-radius: 50%; background: radial-gradient(ellipse, rgba(0,0,0,.28), rgba(0,0,0,0) 70%); }

  .ad { position: absolute; left: 19px; top: 653px; width: 216px; height: 183px; border: 5px solid #e9e9e9; background: #fff; display: flex; align-items: center; justify-content: center; font-size: 21px; color: #8e8e8e; }

  .rss { position: absolute; left: 51px; top: 862px; width: 152px; height: 42px; border-radius: 21px; background: var(--rss-fill); border: 1px solid #d6c7ae; box-shadow: 0 2px 3px rgba(0,0,0,.2); }
  .rss .dot { position: absolute; left: 0; top: -3px; width: 47px; height: 47px; border-radius: 50%; background: radial-gradient(circle at 40% 35%, #d79a45, #8a5418); border: 2px solid #e6dccb; }
  .rss span { position: absolute; left: 58px; top: 9px; font-size: 20px; color: var(--rss-brown); }

  .footer { position: absolute; left: 0; top: 985px; width: 1200px; text-align: center; color: #fff; font-size: 13.5px; line-height: 16px; }
</style>
</head>
<body>
  <main class="page">
    <div class="top-rule"></div>
    <h2 class="comment-title">What Do You Think?</h2>

    <div class="field" style="top:88px">
      <div class="icon">
        <svg width="28" height="28" viewBox="0 0 28 28" fill="none" stroke="#fff" stroke-width="2.4"><circle cx="14" cy="14" r="11.5"/><circle cx="10.5" cy="11" r="1" fill="#fff"/><circle cx="17.5" cy="11" r="1" fill="#fff"/><path d="M8.5 16q5.5 6 11 0"/></svg>
      </div>
      <span>your name</span>
    </div>
    <div class="field" style="top:144px">
      <div class="icon">
        <svg width="28" height="20" viewBox="0 0 28 20" fill="none" stroke="#fff" stroke-width="2"><rect x="1" y="1" width="26" height="18"/><path d="M1 1l13 11 13-11M1 19l10-9M27 19l-10-9"/></svg>
      </div>
      <span>e-mail</span>
    </div>
    <div class="field" style="top:201px">
      <div class="icon">
        <svg width="28" height="28" viewBox="0 0 28 28" fill="none" stroke="#fff" stroke-width="1.6"><circle cx="14" cy="14" r="12"/><ellipse cx="14" cy="14" rx="5.5" ry="12"/><path d="M2 14h24M14 2v24M4 8h20M4 20h20"/></svg>
      </div>
      <span>web</span>
    </div>
    <div class="field field-comment" style="top:257px"><span>comment</span></div>
    <div class="send">SEND</div>
  </main>

  <aside class="sidebar">
    <div class="recent-comment">
      <div class="avatar" role="img" aria-label="Commenter avatar photo"></div>
      <div class="txt">
        <div class="title">Re: Say no to smoking</div>
        <div class="excerpt">I agree with you dude...</div>
        <div class="date">Posted on 01-01-2010</div>
      </div>
    </div>

    <h3 class="widget-title" style="top:89px">Blogroll</h3>
    <ul class="blogroll">
      <li>Healthy Life</li>
      <li>Health Magazine</li>
      <li>Healthy Life</li>
      <li>Health Magazine</li>
      <li>Healthy Life</li>
    </ul>

    <h3 class="widget-title" style="top:277px">Tag Cloud</h3>
    <div class="tags">
      <span style="font-size:12px">Healthy Life</span>
      <span style="font-size:19px">Smoke</span>
      <span style="font-size:17px">alchohol</span>
      <span style="font-size:14px">cigarette</span>
      <span style="font-size:22px">Health addiction</span>
      <span style="font-size:19px">Dangerous Effect</span>
      <span style="font-size:17px">sport</span>
      <span style="font-size:17px">bad habbit</span>
    </div>

    <div class="tweet">
      About to embark on a browser testing adventure, but I need to get some damn coffee brewing first. What a way to end the week. Have fun everybody...
      <div class="when">1 hr ago</div>
    </div>
    <svg class="tweet-tail" width="60" height="14" viewBox="0 0 60 14"><path d="M0 0l30 12 0-12z" fill="#fff" stroke="#cfcfcf"/><path d="M1 0h28" stroke="#fff" stroke-width="2"/></svg>
    <div class="mascot-shadow"></div>
    <div class="mascot" role="img" aria-label="Blue cartoon bird mascot illustration"></div>

    <div class="ad">ADVERTISEMENT</div>

    <div class="rss">
      <div class="dot"></div>
      <span>rss feed</span>
    </div>
  </aside>

  <footer class="footer">
    copyright (c) www.turningovernewleaves.com 2011<br>allrights reserved
  </footer>

  <div class="grass" role="img" aria-label="Green grass meadow illustration"></div>
</body>
</html>
```